Willowmere Stud website

We would like to create a horse stud/agistment farm website similar to this websites we have attached below:
www.thornbrae.com.au
www.kestlewood.com.au
www.brindlecote.com
www.fenwaite.com.au
The main colour scheme are purple and white to align with the stable's racing colours.
We have also attach the company logo and also images of the farm and create some ideas for the website.
Many thanks for looking into this project!

```html
<!DOCTYPE html>
<html lang="en">
<head>
<meta charset="utf-8">
<title>Willowmere Stud</title>
<link href="https://fonts.googleapis.com/css2?family=Poppins:wght@400;600;700;800&family=Open+Sans:wght@400;600&display=swap" rel="stylesheet">
<style>
:root{
  --purple:#3b1745;
  --purple-dark:#2c1033;
  --ink:#1d1d1f;
  --text:#555;
  --light:#f1f0f1;
  --line:#d9d7da;
  --white:#fff;
  --sky-top:#6fa3e6;
  --sky-low:#cfe0f2;
  --grass:#4f7f35;
}
*{box-sizing:border-box;margin:0;padding:0}
html,body{width:1200px;height:4000px;overflow:hidden}
body{font-family:"Open Sans",sans-serif;color:var(--text);background:var(--white);position:relative}
h1,h2,h3,h4,.nav,.btn,.brand{font-family:"Poppins",sans-serif}
.btn{display:inline-block;background:var(--purple);color:var(--white);font-size:13px;font-weight:600;letter-spacing:.5px;padding:11px 22px;text-transform:uppercase}

/* hero */
.hero{position:absolute;left:0;top:0;width:1200px;height:700px;background:linear-gradient(180deg,var(--sky-top) 0%,var(--sky-low) 55%,#8aa86a 78%,var(--grass) 100%)}
.hero-photo{position:absolute;inset:0}
.site-header{position:absolute;left:0;top:0;width:1200px;height:80px;display:flex;align-items:center;justify-content:space-between;padding:0 40px 0 36px}
.brand{display:flex;align-items:center;gap:12px;font-size:22px;font-weight:700;color:var(--purple);letter-spacing:.5px}
.brand-dot{width:30px;height:30px;border-radius:50%;background:var(--white)}
.nav{display:flex;gap:6px}
.nav a{font-size:13px;font-weight:600;color:var(--white);padding:8px 12px;text-decoration:none}
.nav a.active{background:var(--purple)}
.hero-tag{position:absolute;right:0;top:505px;background:var(--purple);color:var(--white);font-family:"Poppins",sans-serif;font-weight:700;font-size:26px;padding:14px 40px 14px 26px}
.hero-dots{position:absolute;left:0;width:1200px;top:624px;display:flex;justify-content:center;gap:10px}
.hero-dots span{width:10px;height:10px;border-radius:50%;background:rgba(255,255,255,.6)}
.hero-dots span.on{background:var(--white)}

/* section titles */
.section-title{position:absolute;left:0;width:1200px;text-align:center;font-size:34px;font-weight:800;color:var(--ink);letter-spacing:.5px}
.section-title::after{content:"";display:block;width:170px;height:3px;background:var(--ink);margin:2px auto 0}

/* stallions */
.stallions{position:absolute;left:20px;top:860px;width:1164px;height:332px;display:flex;gap:10px}
.stallion{flex:1;position:relative}
.stallion .photo{position:absolute;inset:0}
.stallion .caption{position:absolute;left:18px;bottom:18px;color:var(--white);font-family:"Poppins",sans-serif;font-weight:700;font-size:16px}

/* welcome */
.welcome{position:absolute;left:0;top:1232px;width:1200px;height:628px;background:var(--light)}
.welcome-frame{position:absolute;left:144px;top:48px;width:536px;height:480px;border:6px solid var(--line)}
.welcome-copy{position:absolute;left:190px;top:100px;width:230px}
.welcome-copy h2{font-size:30px;line-height:1.1;font-weight:800;color:var(--ink)}
.welcome-copy .rule{width:40px;height:3px;background:var(--purple);margin:14px 0}
.welcome-copy p{font-size:14px;line-height:1.5;margin-bottom:22px}
.welcome-watermark{position:absolute;left:770px;top:40px;font-family:"Poppins",sans-serif;font-weight:800;font-size:62px;line-height:.95;color:#e3e1e4}
.welcome-photo{position:absolute;left:720px;top:250px;width:420px;height:320px;background:linear-gradient(180deg,#8a4a24 0%,#6c3718 70%,#d8d6d8 100%)}

/* news */
.news{position:absolute;top:2040px;left:128px;width:944px;display:flex;gap:36px}
.news-card{width:290px;height:460px;background:var(--light);position:relative}
.news-card .photo{height:208px}
.news-card h3{background:var(--purple);color:var(--white);font-size:15px;font-weight:700;line-height:1.3;padding:10px 20px;margin:0 0 16px 20px}
.news-card p{font-size:13px;line-height:1.5;padding:0 20px 18px}
.news-card .btn{margin-left:20px;font-size:11px;padding:8px 16px}

/* video */
.video{position:absolute;left:0;top:2580px;width:1200px;height:560px;background:linear-gradient(90deg,var(--light) 0%,#d7d8d6 100%)}
.video-panel{position:absolute;left:0;top:0;width:520px;height:560px;background:var(--light)}
.video-copy{position:absolute;left:144px;top:160px;width:260px}
.video-copy h2{font-size:32px;font-weight:800;color:var(--ink)}
.video-copy h2::after{content:"";display:block;width:200px;height:3px;background:var(--ink);margin:2px 0 26px}
.video-copy p{font-family:"Poppins",sans-serif;font-weight:700;font-size:18px;line-height:1.4;color:var(--ink);margin-bottom:30px}
.video-frame{position:absolute;left:432px;top:40px;width:628px;height:460px;border-left:10px solid var(--purple);background:linear-gradient(180deg,#c9cbcb 0%,#a9aeab 40%,#5d7f3b 55%,#496e2e 100%)}
.play{position:absolute;left:280px;top:185px}

/* call to action */
.cta{position:absolute;left:0;top:3148px;width:1200px;height:392px;background:radial-gradient(ellipse at 50% 70%,#5b5a3f 0%,#2a3220 45%,#141a11 100%)}
.cta-inner{position:absolute;left:0;top:128px;width:1200px;text-align:center}
.cta-inner h2{font-size:30px;font-weight:700;line-height:1.35;color:var(--white);margin-bottom:28px}
.btn-outline{display:inline-block;border:2px solid var(--white);color:var(--white);font-family:"Poppins",sans-serif;font-size:13px;font-weight:600;padding:10px 24px}

/* footer */
.site-footer{position:absolute;left:0;top:3540px;width:1200px;height:460px;background:var(--purple-dark);color:#d8cfdc}
.footer-col h4{font-size:12px;font-weight:700;color:var(--white);margin-bottom:22px;letter-spacing:.5px}
.footer-contact{position:absolute;left:140px;top:74px}
.footer-social{position:absolute;left:944px;top:74px}
.footer-item{display:flex;align-items:center;gap:12px;font-size:12px;margin-bottom:16px}
.footer-item .dot{width:22px;height:22px;border-radius:50%;background:var(--white);flex:none;display:flex;align-items:center;justify-content:center}
.footer-brand{position:absolute;left:0;width:1200px;top:90px;display:flex;flex-direction:column;align-items:center;gap:14px}
.footer-brand .mark{width:120px;height:120px;border-radius:50%;border:3px solid var(--white)}
.footer-brand .name{font-family:"Poppins",sans-serif;font-weight:700;font-size:20px;color:var(--white);letter-spacing:1px}
.footer-links{position:absolute;left:0;width:1200px;top:316px;display:flex;justify-content:center;gap:22px;font-size:12px}
.footer-rule{position:absolute;left:330px;width:540px;top:356px;height:1px;background:rgba(255,255,255,.25)}
.copyright{position:absolute;left:0;width:1200px;top:414px;text-align:center;font-size:11px}
</style>
</head>
<body>

<section class="hero">
  <div class="hero-photo" role="img" aria-label="Five horses standing in a green paddock under a blue sky"></div>
  <header class="site-header">
    <div class="brand"><span class="brand-dot"></span>WILLOWMERE STUD</div>
    <nav class="nav">
      <a class="active">HOME</a><a>ABOUT US</a><a>NEWS</a><a>STALLIONS</a><a>VIDEOS</a><a>GALLERY</a><a>CONTACT US</a>
    </nav>
  </header>
  <div class="hero-tag">HORSE STUD FARM</div>
  <div class="hero-dots"><span class="on"></span><span></span><span></span><span></span></div>
</section>

<h2 class="section-title" style="top:760px">STALLIONS</h2>
<section class="stallions">
  <div class="stallion"><div class="photo" role="img" aria-label="Grey horse in a paddock" style="background:linear-gradient(160deg,#9bb37c,#c9b89a 55%,#4f6b33)"></div><span class="caption">LOREM IPSUM</span></div>
  <div class="stallion"><div class="photo" role="img" aria-label="Bay horse by a driveway" style="background:linear-gradient(160deg,#d6d9d4,#8b4a2b 55%,#6e7d5a)"></div><span class="caption">LOREM IPSUM</span></div>
  <div class="stallion"><div class="photo" role="img" aria-label="Chestnut horse on green pasture" style="background:linear-gradient(180deg,#3f6a2a,#6d8f3c 50%,#4d7a2c)"></div><span class="caption">LOREM IPSUM</span></div>
  <div class="stallion"><div class="photo" role="img" aria-label="Grey horse being held by a handler" style="background:linear-gradient(160deg,#7fa7d8,#9aa0a6 50%,#5a5e63)"></div><span class="caption">LOREM IPSUM</span></div>
</section>

<section class="welcome">
  <div class="welcome-watermark">WILLOW<br>MERE<br>STUD</div>
  <div class="welcome-frame"></div>
  <div class="welcome-copy">
    <h2>WELCOME TO<br>OUR SITE</h2>
    <div class="rule"></div>
    <p>Lorem ipsum dolor sit amet, consectetur adipiscing elit, sed do eiusmod tempor incididunt ut labore et dolore magna aliqua. Ut enim ad minim veniam, quis nostrud exercitation ullamco laboris nisi ut aliquip ex ea commodo consequat. Duis aute irure dolor in reprehenderit.</p>
    <span class="btn">READ MORE</span>
  </div>
  <div class="welcome-photo" role="img" aria-label="Bay thoroughbred horse standing in profile"></div>
</section>

<h2 class="section-title" style="top:1936px">RECENT NEWS</h2>
<section class="news">
  <article class="news-card">
    <div class="photo" role="img" aria-label="Mares grazing in a paddock" style="background:linear-gradient(180deg,#a9c0d6,#5f8a3a 45%,#3d6826)"></div>
    <h3>LOREM IPSUM DOLOR<br>SIT AMET</h3>
    <p>Sed ut perspiciatis unde omnis iste natus error sit voluptatem accusantium doloremque laudantium, totam rem aperiam, eaque ipsa.</p>
    <span class="btn">READ MORE</span>
  </article>
  <article class="news-card">
    <div class="photo" role="img" aria-label="Racehorse and jockey in purple silks" style="background:linear-gradient(180deg,#b06a3a,#7a3f7e 40%,#d9d3c8 70%,#4f8a3a)"></div>
    <h3>LOREM IPSUM DOLOR<br>SIT AMET</h3>
    <p>Sed ut perspiciatis unde omnis iste natus error sit voluptatem accusantium doloremque laudantium, totam rem aperiam, eaque ipsa.</p>
    <span class="btn">READ MORE</span>
  </article>
  <article class="news-card">
    <div class="photo" role="img" aria-label="Aerial view of the farm buildings and paddocks" style="background:linear-gradient(180deg,#9fc0e0,#7fa35a 40%,#c8c3b6 70%,#5d8a3a)"></div>
    <h3>LOREM IPSUM DOLOR<br>SIT AMET</h3>
    <p>Sed ut perspiciatis unde omnis iste natus error sit voluptatem accusantium doloremque laudantium, totam rem aperiam, eaque ipsa.</p>
    <span class="btn">READ MORE</span>
  </article>
</section>

<section class="video">
  <div class="video-panel"></div>
  <div class="video-frame" role="img" aria-label="Grey horse standing in a field under a cloudy sky">
    <svg class="play" width="68" height="68" viewBox="0 0 68 68"><circle cx="34" cy="34" r="32" fill="#fff"/><path d="M27 21 L49 34 L27 47 Z" fill="#1d1d1f"/></svg>
  </div>
  <div class="video-copy">
    <h2>OUR VIDEO</h2>
    <p>Sed ut perspiciatis unde omnis iste natus error sit voluptatem accusantium</p>
    <span class="btn">WATCH VIDEO</span>
  </div>
</section>

<section class="cta" role="img" aria-label="Tree-lined farm driveway at dusk">
  <div class="cta-inner">
    <h2>Sed ut perspiciatis unde omnis<br>iste natus error sit voluptatem.</h2>
    <span class="btn-outline">CONTACT US</span>
  </div>
</section>

<footer class="site-footer">
  <div class="footer-col footer-contact">
    <h4>CONTACT US</h4>
    <div class="footer-item"><span class="dot"><svg width="10" height="12" viewBox="0 0 10 12"><path d="M5 0a4 4 0 0 0-4 4c0 3 4 8 4 8s4-5 4-8a4 4 0 0 0-4-4z" fill="#2c1033"/></svg></span>Willowbank Road,<br>Bellbrook NSW 2440</div>
    <div class="footer-item"><span class="dot"><svg width="10" height="10" viewBox="0 0 10 10"><path d="M2 0l2 2-1 2c1 1 2 2 3 3l2-1 2 2-2 2C4 10 0 6 0 2z" fill="#2c1033"/></svg></span>+61 2 6555 0148</div>
    <div class="footer-item"><span class="dot"><svg width="12" height="9" viewBox="0 0 12 9"><rect x=".5" y=".5" width="11" height="8" fill="none" stroke="#2c1033"/><path d="M.5.5L6 5l5.5-4.5" fill="none" stroke="#2c1033"/></svg></span>info@willowmerestud.com.au</div>
  </div>
  <div class="footer-brand"><div class="mark"></div><div class="name">WILLOWMERE STUD</div></div>
  <div class="footer-col footer-social">
    <h4>CONNECT WITH US</h4>
    <div class="footer-item"><span class="dot"></span>Pagebook</div>
    <div class="footer-item"><span class="dot"></span>Chirper</div>
    <div class="footer-item"><span class="dot"></span>Linkwork</div>
  </div>
  <nav class="footer-links"><span>Home</span><span>About Us</span><span>News</span><span>Stallions</span><span>Videos</span><span>Gallery</span><span>Contact Us</span></nav>
  <div class="footer-rule"></div>
  <p class="copyright">Copyright © 2019 All Rights Reserved</p>
</footer>

</body>
</html>
```